PawQuarry Banner contest an ecommerce site for veterinarians

We need banners for our ecommerce site. Our site is a webstore that veterinarians can use to allow their clients to purchase items from them. Each month we have a different theme for our banners. I am looking for banners for January and February and with a refresh coming to our site could be looking at a dozen over the next year. I may potentially choose from multiple designers and increase the payment or will choose one designer for both months .

For January our theme is winter fun. We will be running a contest were people can submit a picture of their pet to our Chatterloop page enjoying the snow or keeping warm. they have a chance to win one of 5 $50 gift certificates to pawquarry. The banner should have a dog and cat and a separate one with just a cat. We will need a French and English banner. We will provide the French translation once the winner has been selected.

For February our theme is dental health. The banner should have a dog and cat and a separate one with just a cat. We will need a French and English banner. We will provide the French translation once the winner has been selected.

Target Market(s)

pet owners

Industry/Entity Type

Veterinary

Colors

Designer to choose colors to be used in the design.

Requirements
Must have
• dimensions for PQ Banner are: 710px x 280px
Nice to have
• I have attached our logo and some screen shoots of our site so you can get a feel of what it look like. you could also go to www.pawquarry.ca and see what the sign in page looks like
Should not have
• images of pet food

```html
<!DOCTYPE html>
<html lang="en">
<head>
<meta charset="utf-8">
<title>PawQuarry banners – January &amp; February</title>
<link rel="stylesheet" href="https://fonts.googleapis.com/css2?family=Montserrat:wght@400;600;700;800&family=Open+Sans:wght@400;600;700&display=swap">
<style>
  :root {
    --canvas: #2b2321;
    --ice: #eef4f8;
    --ice-deep: #d7e5ee;
    --red: #e31e2d;
    --red-dark: #c4141f;
    --navy: #1d2d5a;
    --ink: #2f3640;
    --sky: #2aa3dc;
    --sky-deep: #1a86c4;
    --sun: #f8e84a;
    --white: #ffffff;
  }
  * { box-sizing: border-box; margin: 0; padding: 0; }
  html, body { width: 711px; height: 1200px; overflow: hidden; background: var(--canvas); }
  body { position: relative; font-family: "Open Sans", Arial, sans-serif; }

  .banner { position: absolute; left: 66px; width: 580px; height: 238px; overflow: hidden; }
  .banner--jan-cat { top: 68px; }
  .banner--jan-duo { top: 330px; }
  .banner--feb-group { top: 604px; }
  .banner--feb-dog { top: 868px; }

  /* January */
  .winter { background: linear-gradient(180deg, var(--white) 0%, var(--ice) 55%, var(--ice-deep) 100%); }
  .winter .prize-band { position: absolute; left: 0; right: 0; bottom: 0; height: 70px; background: var(--red); }
  .winter .photo {
    position: absolute; background: var(--white); padding: 7px;
    box-shadow: 0 4px 10px rgba(0,0,0,.25);
  }
  .winter .photo .fill { width: 100%; height: 100%; }
  .photo--cat-single { left: 32px; top: 14px; width: 190px; height: 164px; transform: rotate(-5deg); }
  .photo--dog { left: 18px; top: 18px; width: 150px; height: 150px; transform: rotate(-6deg); }
  .photo--cat-pair { left: 140px; top: 20px; width: 120px; height: 152px; transform: rotate(4deg); }
  .fill--cat-xmas { background: linear-gradient(135deg, #c92a2a 0%, #8e8a85 45%, #d9d4cc 70%, #2e6b3a 100%); }
  .fill--dog-reindeer { background: linear-gradient(135deg, #e9e4dc 0%, #6b3f24 45%, #c0242b 100%); }

  .winter .copy { position: absolute; left: 290px; top: 44px; width: 270px; }
  .winter .title {
    font-family: "Montserrat", Arial, sans-serif; font-weight: 800;
    color: var(--red); font-size: 31px; line-height: 1.02; letter-spacing: -.5px;
  }
  .winter .lede { margin-top: 8px; font-size: 11.5px; line-height: 1.35; color: var(--ink); }
  .winter .tag {
    position: absolute; left: 290px; bottom: 56px;
    background: var(--navy); color: var(--white);
    font-family: "Montserrat", Arial, sans-serif; font-weight: 700; font-size: 9.5px;
    letter-spacing: .6px; padding: 4px 9px;
  }
  .winter .prize {
    position: absolute; left: 290px; bottom: 14px; width: 270px;
    color: var(--white); font-size: 11px; font-weight: 600; line-height: 1.35;
  }

  .brand {
    position: absolute; display: flex; align-items: center; gap: 5px;
    font-family: "Montserrat", Arial, sans-serif; font-weight: 700; font-size: 14px;
  }
  .brand .mark { width: 10px; height: 10px; }
  .winter .brand { right: 18px; top: 14px; color: var(--red-dark); }
  .winter .brand .mark { background: var(--red-dark); }

  /* February */
  .dental { background: linear-gradient(180deg, var(--sky) 0%, var(--sky-deep) 100%); }
  .dental .brand { left: 26px; top: 18px; color: var(--white); }
  .dental .brand .mark { background: var(--white); border-radius: 50%; }
  .dental .copy { position: absolute; left: 26px; top: 72px; width: 230px; }
  .dental .title {
    font-family: "Montserrat", Arial, sans-serif; font-weight: 800;
    font-size: 30px; line-height: 1.02; letter-spacing: -.5px; color: var(--white);
  }
  .dental .title .accent { color: var(--sun); display: block; }
  .dental .lede { margin-top: 10px; font-size: 11px; line-height: 1.4; color: var(--white); }
  .dental .pets { position: absolute; }
  .pets--group { left: 268px; top: 20px; width: 300px; height: 218px;
    background: linear-gradient(120deg, rgba(217,180,130,.9) 0%, rgba(180,120,70,.9) 50%, rgba(90,70,60,.85) 100%);
    border-radius: 120px 120px 0 0; }
  .pets--dog { left: 250px; top: 14px; width: 250px; height: 224px;
    background: linear-gradient(160deg, rgba(250,250,250,.95) 0%, rgba(190,120,60,.9) 55%, rgba(60,60,60,.9) 100%);
    border-radius: 110px 110px 0 0; }
</style>
</head>
<body>

  <section class="banner winter banner--jan-cat" aria-label="January photo contest banner with a cat">
    <div class="prize-band"></div>
    <div class="photo photo--cat-single"><div class="fill fill--cat-xmas" role="img" aria-label="Photo of a tabby cat in a Santa hat beside a decorated Christmas tree"></div></div>
    <div class="brand"><span class="mark"></span>PawQuarry</div>
    <div class="copy">
      <h2 class="title">January<br>Photo Contest</h2>
      <p class="lede">Submit your best photo together with your pet enjoying the snow or keeping warm this holiday season to our Chatterloop page!</p>
    </div>
    <span class="tag">WHAT YOU GET</span>
    <p class="prize">Lucky contestants will win one of 5 $50 gift certificates to pawquarry.ca</p>
  </section>

  <section class="banner winter banner--jan-duo" aria-label="January photo contest banner with a dog and a cat">
    <div class="prize-band"></div>
    <div class="photo photo--dog"><div class="fill fill--dog-reindeer" role="img" aria-label="Photo of a brown dog wearing reindeer antlers and a red scarf"></div></div>
    <div class="photo photo--cat-pair"><div class="fill fill--cat-xmas" role="img" aria-label="Photo of a tabby cat in a Santa hat"></div></div>
    <div class="brand"><span class="mark"></span>PawQuarry</div>
    <div class="copy">
      <h2 class="title">January<br>Photo Contest</h2>
      <p class="lede">Submit your best photo together with your pet enjoying the snow or keeping warm this holiday season to our Chatterloop page!</p>
    </div>
    <span class="tag">WHAT YOU GET</span>
    <p class="prize">Lucky contestants will win one of 5 $50 gift certificates to pawquarry.ca</p>
  </section>

  <section class="banner dental banner--feb-group" aria-label="February dental month banner with dog and cats">
    <div class="brand"><span class="mark"></span>PawQuarry</div>
    <div class="copy">
      <h2 class="title"><span class="accent">Dental Month</span>this February</h2>
      <p class="lede">To learn how much teeth affects overall health. Talk to your veterinarian and schedule a dental exam today.</p>
    </div>
    <div class="pets pets--group" role="img" aria-label="Photo of a beagle puppy sitting with three kittens"></div>
  </section>

  <section class="banner dental banner--feb-dog" aria-label="February dental month banner with a dog">
    <div class="brand"><span class="mark"></span>PawQuarry</div>
    <div class="copy">
      <h2 class="title"><span class="accent">Dental Month</span>this February</h2>
      <p class="lede">To learn how much teeth affects overall health. Talk to your veterinarian and schedule a dental exam today.</p>
    </div>
    <div class="pets pets--dog" role="img" aria-label="Photo of a terrier holding a blue toothbrush in its mouth"></div>
  </section>

</body>
</html>
```